Tea towel Design

Every year, we design a tea towel to celebrate our business anniversary. A boutique real estate business. www.larnix.co
I need two different designs for 2023 and 2024.

The anniversary date is 16th June.

I have attached the logos and the tea towels we used previously.

Size: 50 x 70cm Print area: 40 x 60cm (artwork portrait)

Colours: Tangerine - #ed5338 - Denim - #003366

Target Market(s)

Tea Towels are used as gift for our clients in their settlement package.

Industry/Entity Type

Real Estate.

Requirements
Must have
• a great look, the captures our business culture
Should not have
• things not related to our business

```html
<!DOCTYPE html>
<html lang="en">
<head>
<meta charset="UTF-8">
<title>Larnix &amp; Co. 4th Anniversary Tea Towel</title>
<link rel="stylesheet" href="https://fonts.googleapis.com/css2?family=Outfit:wght@500;600;700&display=swap">
<style>
  :root {
    --denim: #003366;
    --tangerine: #ed5338;
    --white: #ffffff;
    --ink-deep: #0a2648;
    --ink-fade: #0f3d78;
    --ink-bright: #1b5cb8;
  }
  * { margin: 0; padding: 0; box-sizing: border-box; }
  html, body {
    width: 900px;
    height: 1200px;
    overflow: hidden;
    background: var(--denim);
  }
  .towel {
    width: 900px;
    height: 1200px;
    background: var(--denim);
    display: grid;
    grid-template-columns: repeat(3, 1fr);
    grid-template-rows: repeat(11, 1fr);
    padding: 20px 10px 24px;
    font-family: "Outfit", sans-serif;
  }
  .wordmark {
    display: flex;
    align-items: center;
    justify-content: center;
    font-weight: 600;
    font-size: 40px;
    letter-spacing: 0.2px;
    white-space: nowrap;
    padding-top: 28px;
  }
  .wordmark--deep { color: var(--ink-deep); }
  .wordmark--fade { color: var(--ink-fade); }
  .wordmark--bright { color: var(--ink-bright); }
  .wordmark--feature { color: var(--white); }
  .anniversary {
    display: flex;
    flex-direction: column;
    align-items: center;
    justify-content: center;
    padding-top: 28px;
    font-weight: 700;
    line-height: 1.2;
  }
  .anniversary__title {
    color: var(--white);
    font-size: 25px;
    letter-spacing: 0.5px;
  }
  .anniversary__date {
    color: var(--tangerine);
    font-size: 25px;
    letter-spacing: 0.3px;
  }
</style>
</head>
<body>
<main class="towel">
  <!-- row 1 -->
  <div class="wordmark wordmark--deep">Larnix &amp; Co.</div>
  <div class="wordmark wordmark--deep">Larnix &amp; Co.</div>
  <div class="wordmark wordmark--deep">Larnix &amp; Co.</div>
  <!-- row 2 -->
  <div class="wordmark wordmark--deep">Larnix &amp; Co.</div>
  <div class="wordmark wordmark--deep">Larnix &amp; Co.</div>
  <div class="wordmark wordmark--deep">Larnix &amp; Co.</div>
  <!-- row 3 -->
  <div class="wordmark wordmark--deep">Larnix &amp; Co.</div>
  <div class="wordmark wordmark--deep">Larnix &amp; Co.</div>
  <div class="wordmark wordmark--deep">Larnix &amp; Co.</div>
  <!-- row 4 -->
  <div class="wordmark wordmark--deep">Larnix &amp; Co.</div>
  <div class="wordmark wordmark--deep">Larnix &amp; Co.</div>
  <div class="wordmark wordmark--fade">Larnix &amp; Co.</div>
  <!-- row 5 -->
  <div class="wordmark wordmark--deep">Larnix &amp; Co.</div>
  <div class="wordmark wordmark--fade">Larnix &amp; Co.</div>
  <div class="wordmark wordmark--bright">Larnix &amp; Co.</div>
  <!-- row 6 -->
  <div class="wordmark wordmark--deep">Larnix &amp; Co.</div>
  <div class="wordmark wordmark--feature">Larnix &amp; Co.</div>
  <div class="wordmark wordmark--bright">Larnix &amp; Co.</div>
  <!-- row 7 -->
  <div class="wordmark wordmark--fade">Larnix &amp; Co.</div>
  <div class="wordmark wordmark--bright">Larnix &amp; Co.</div>
  <div class="wordmark wordmark--bright">Larnix &amp; Co.</div>
  <!-- row 8 -->
  <div class="wordmark wordmark--bright">Larnix &amp; Co.</div>
  <div class="wordmark wordmark--bright">Larnix &amp; Co.</div>
  <div class="wordmark wordmark--bright">Larnix &amp; Co.</div>
  <!-- row 9 -->
  <div class="wordmark wordmark--bright">Larnix &amp; Co.</div>
  <div class="wordmark wordmark--bright">Larnix &amp; Co.</div>
  <div class="wordmark wordmark--bright">Larnix &amp; Co.</div>
  <!-- row 10 -->
  <div class="wordmark wordmark--bright">Larnix &amp; Co.</div>
  <div class="anniversary">
    <span class="anniversary__title">4th ANNIVERSARY</span>
    <span class="anniversary__date">16TH JUNE 2024</span>
  </div>
  <div class="wordmark wordmark--bright">Larnix &amp; Co.</div>
  <!-- row 11 -->
  <div class="wordmark wordmark--bright">Larnix &amp; Co.</div>
  <div class="wordmark wordmark--bright">Larnix &amp; Co.</div>
  <div class="wordmark wordmark--bright">Larnix &amp; Co.</div>
</main>
</body>
</html>
```